A new presentation to our clients

we are a Real Estate agency, our website is www.dorelumia.com and it’s time to have a new, fashion and remarcable Business Card. we want to differentiate ourselves from other companies so we want a business card that differentiates us. we want the business card to impact our customers. in the competitive market that we have today, we have to be different and it is this difference that we seek

Target Market(s)

Real Estate Clients

Contact Information for Business Card

We search a totaly diferent card from the usual

Font styles to use
Sans Serif

Colors
e34197

Requirements
Must have
• Logo, adress, phone contact, e-mail, photo, and our website
Nice to have
• We would like to see a modern business card
Should not have
• Houses or building draws

```html
<!DOCTYPE html>
<html lang="en">
<head>
<meta charset="utf-8">
<title>Dore Lumia — Business Card</title>
<link href="https://fonts.googleapis.com/css2?family=Roboto:ital,wght@0,300;0,400;0,500;0,700;1,300&display=swap" rel="stylesheet">
<style>
  :root {
    --stage: #262627;
    --card-dark: #474a54;
    --brand-pink: #e8317a;
    --pink-soft: #ef5a93;
    --pink-deep: #c93a6c;
    --text-light: #ffffff;
    --text-muted: #e6e6ea;
  }
  * { margin: 0; padding: 0; box-sizing: border-box; }
  html, body { width: 1200px; height: 1200px; overflow: hidden; }
  body {
    background: radial-gradient(ellipse at 50% 40%, #323233 0%, var(--stage) 70%);
    font-family: 'Roboto', Arial, sans-serif;
    position: relative;
  }
  .card {
    position: absolute;
    left: 140px;
    width: 920px;
    height: 524px;
    border-radius: 30px;
    overflow: hidden;
    box-shadow: 0 18px 40px rgba(0,0,0,0.55), 0 4px 10px rgba(0,0,0,0.35);
  }
  .card-front { top: 48px; background: var(--card-dark); }
  .card-back  { top: 640px; background: var(--brand-pink); }

  .wordmark {
    position: absolute;
    font-weight: 500;
    letter-spacing: 1px;
    white-space: nowrap;
    line-height: 1;
  }
  .card-front .wordmark { left: 42px; top: 92px; font-size: 112px; color: var(--brand-pink); }
  .card-back .wordmark {
    left: 0; right: 0; top: 196px; text-align: center;
    font-size: 132px; color: var(--text-light);
  }

  .holder { position: absolute; left: 42px; top: 310px; }
  .holder-name { font-size: 35px; font-weight: 500; color: var(--text-light); }
  .holder-role { font-size: 22px; font-weight: 300; font-style: italic; color: var(--brand-pink); margin-top: 6px; }

  .contact-list { position: absolute; left: 46px; top: 398px; list-style: none; }
  .contact-list li {
    display: flex; align-items: center; height: 30px;
    font-size: 20px; font-weight: 300; color: var(--text-muted);
  }
  .contact-list svg { width: 20px; height: 20px; margin-right: 24px; fill: var(--brand-pink); }

  .office { position: absolute; right: 95px; top: 372px; text-align: right; }
  .office-address { font-size: 21px; font-weight: 300; color: var(--text-muted); line-height: 22px; }
  .office-web { font-size: 20px; font-weight: 300; color: var(--text-muted); margin-top: 24px; }
  .office-web span { color: var(--brand-pink); }

  .back-texture {
    position: absolute; inset: 0;
    background:
      radial-gradient(ellipse 60% 18% at 30% 40%, rgba(255,255,255,0.10), transparent 70%),
      radial-gradient(ellipse 50% 15% at 75% 65%, rgba(150,30,80,0.18), transparent 70%),
      radial-gradient(ellipse 70% 20% at 50% 85%, rgba(255,255,255,0.08), transparent 70%),
      linear-gradient(160deg, var(--brand-pink) 0%, var(--pink-soft) 50%, var(--brand-pink) 100%);
  }
</style>
</head>
<body>
  <section class="card card-front">
    <div class="wordmark">Dore Lumia</div>

    <div class="holder">
      <div class="holder-name">Mara Velin</div>
      <div class="holder-role">manager</div>
    </div>

    <ul class="contact-list">
      <li>
        <svg viewBox="0 0 20 20" aria-hidden="true"><path d="M5 0h10a2 2 0 0 1 2 2v16a2 2 0 0 1-2 2H5a2 2 0 0 1-2-2V2a2 2 0 0 1 2-2zm0 3v12h10V3zm5 13.5a1 1 0 1 0 0 2 1 1 0 0 0 0-2z"/></svg>
        +123 - 456 - 9789
      </li>
      <li>
        <svg viewBox="0 0 20 20" aria-hidden="true"><path d="M1 7c0-2 4-4 9-4s9 2 9 4v2h-4V7.5c-1.5-.6-3.2-.8-5-.8s-3.5.2-5 .8V9H1zm5 2h8l3 8H3z"/></svg>
        +123 - 456 - 9789
      </li>
      <li>
        <svg viewBox="0 0 20 20" aria-hidden="true"><path d="M1 4h18v12H1zm2 2v.4l7 5 7-5V6l-7 5z"/></svg>
        here@yourmail.com
      </li>
    </ul>

    <div class="office">
      <div class="office-address">Ridgeway Court 7<br>1418 Alder<br>Lane Westbrook</div>
      <div class="office-web">www.<span>yourwebsite</span>.com</div>
    </div>
  </section>

  <section class="card card-back">
    <div class="back-texture" role="img" aria-label="Abstract flowing pink marbled swirl pattern"></div>
    <div class="wordmark">Dore Lumia</div>
  </section>
</body>
</html>
```